Thai Takeaway Menu Design

I need a menu re-design for a thai takeaway/restaurant in australia.

Please use content from the existing menu
http://www.platterwink.example/u/menu/7302918?p=1

I'd like to emphasise on
1 - free delivery for order over $40
2 - gluten free and vegetatian option available on most meal (however you want to word it - not fuss)

*remove (the banner order online and save $10)

I'm happy to change the whole concept & design. I particularly like rustic, raw look more than moden ones. Does not need to be flowery or anything like current one :)

Industry/Entity Type

Restaurant

```html
<!DOCTYPE html>
<html lang="en">
<head>
<meta charset="utf-8">
<title>Sawa Traditional Thai Cuisine – Menu</title>
<link rel="stylesheet" href="https://fonts.googleapis.com/css2?family=Arimo:ital,wght@0,400;0,700;1,700&display=swap">
<style>
  :root{
    --deep-red:#6e0906;
    --red:#a3170d;
    --orange:#e4561a;
    --orange-light:#f6892e;
    --yellow:#f8d31e;
    --cream:#fff4dc;
    --white:#ffffff;
  }
  *{box-sizing:border-box;margin:0;padding:0}
  html,body{width:826px;height:1200px;overflow:hidden;background:var(--deep-red)}
  body{font-family:"Arimo",Arial,sans-serif;color:var(--white)}
  .menu{position:relative;width:826px;height:1200px;overflow:hidden;
    background:
      radial-gradient(ellipse 60% 40% at 30% 45%, rgba(246,137,46,.75), transparent 70%),
      radial-gradient(ellipse 50% 35% at 75% 60%, rgba(228,86,26,.7), transparent 70%),
      linear-gradient(180deg,var(--red) 0%,var(--orange) 45%,var(--red) 80%,var(--deep-red) 100%);}
  .food-menu{position:absolute;left:14px;top:10px;width:395px;height:1180px;border:2px solid rgba(255,200,150,.55)}
  .section-title{position:absolute;left:125px;width:180px;height:34px;background:linear-gradient(180deg,var(--orange-light),var(--orange));
    border:2px solid var(--cream);color:var(--white);font-weight:700;font-size:18px;display:flex;align-items:center;justify-content:center}
  .item-list{position:absolute;left:20px;width:355px;background:rgba(110,9,6,.78);border:2px solid var(--orange-light);
    padding:10px 16px;list-style:none;font-size:15px;font-weight:700;line-height:22px}
  .item-list li{display:flex;justify-content:space-between;white-space:nowrap}
  .brand-small{position:absolute;left:30px;top:1080px;width:160px;height:50px;background:var(--yellow);
    display:flex;align-items:center;justify-content:center;font-weight:700;font-size:28px;color:var(--red);letter-spacing:3px}
  .dietary-note{position:absolute;left:20px;top:1150px;font-size:14px}
  .dish-photo{position:absolute;left:427px;top:0;width:399px;height:240px;
    background:radial-gradient(ellipse 55% 60% at 55% 55%, #d9581e, #7a1a0a 60%, #2e0804 100%)}
  .slogan{position:absolute;left:427px;top:268px;width:399px;text-align:center;font-size:22px}
  .brand-box{position:absolute;left:437px;top:333px;width:375px;height:170px;background:var(--yellow);
    display:flex;flex-direction:column;align-items:center;justify-content:center}
  .brand-name{font-weight:700;font-size:74px;color:var(--red);letter-spacing:10px;line-height:1}
  .brand-tagline{font-size:24px;color:var(--red);margin-top:10px}
  .services{position:absolute;left:427px;top:528px;width:399px;text-align:center;font-size:22px;font-weight:700}
  .delivery-offer{position:absolute;left:450px;top:572px;width:352px;height:124px;border:2px solid var(--orange-light);
    background:rgba(110,9,6,.35);color:var(--yellow);font-style:italic;font-weight:700;font-size:21px;line-height:32px;
    display:flex;flex-direction:column;align-items:center;justify-content:center;text-align:center}
  .hours-title{position:absolute;left:530px;top:746px;width:195px;height:44px;background:var(--red);border:2px solid var(--cream);
    font-size:22px;display:flex;align-items:center;justify-content:center}
  .hours{position:absolute;left:427px;top:818px;width:399px;text-align:center;font-size:17px;line-height:28px}
  .hours b{color:var(--yellow)}
  .phone{position:absolute;left:527px;top:974px;width:270px;height:70px;background:var(--white);border-radius:14px;
    color:var(--red);display:flex;align-items:center;justify-content:center;gap:10px;font-weight:700}
  .phone small{font-size:16px}
  .phone span{font-size:34px}
  .address{position:absolute;left:427px;top:1082px;width:399px;text-align:center;font-size:17px;line-height:25px;font-style:normal}
</style>
</head>
<body>
<main class="menu">
  <section class="food-menu">
    <h2 class="section-title" style="top:22px">Dessert</h2>
    <ul class="item-list" style="top:62px">
      <li><span>Black Sticky Rice/w</span></li>
      <li><span>Coconut Cream</span><span>$4.50</span></li>
      <li><span>Tapioca Pudding/w Lychee</span><span>$4.50</span></li>
    </ul>
    <h2 class="section-title" style="top:186px">Drinks</h2>
    <ul class="item-list" style="top:226px">
      <li><span>Cola, Diet Cola, Orangeade, Lemonade</span></li>
      <li><span>Lemon Squash - 375ml</span><span>$2.00</span></li>
      <li><span>Cola, Orangeade, Lemonade - 1.25L</span><span>$4.50</span></li>
      <li><span>Orange Juice, Apple Juice</span><span>$3.50</span></li>
      <li><span>Ginger Beer</span><span>$3.50</span></li>
    </ul>
    <h2 class="section-title" style="top:414px">Dinner for two</h2>
    <ul class="item-list" style="top:454px">
      <li><span>Spring Rolls (4)</span></li>
      <li><span>Chicken &amp; Cashew Nuts</span></li>
      <li><span>Massaman Curry</span></li>
      <li><span>Rice</span><span>$28</span></li>
    </ul>
    <h2 class="section-title" style="top:596px">Family Pack</h2>
    <ul class="item-list" style="top:636px">
      <li><span>Spring Rools (4)</span></li>
      <li><span>Satay Chicken (4)</span></li>
      <li><span>Chicken &amp; Cashew Nuts</span></li>
      <li><span>Red Curry Beef</span></li>
      <li><span>Pad Thai</span></li>
      <li><span>Rice (L)</span><span>$45</span></li>
    </ul>
    <h2 class="section-title" style="top:826px">Lunch Special</h2>
    <ul class="item-list" style="top:866px">
      <li><span>Pad Thai</span></li>
      <li><span>Sweet &amp; Sour Pork/w Rice</span></li>
      <li><span>Chicken &amp; Cashew Nuts/w Rice</span></li>
      <li><span>Green Curry Chicken/w Rice</span></li>
      <li><span>Beef Noodle Soup</span></li>
      <li><span>(Free Can of Soft Drink)</span><span>$10</span></li>
    </ul>
  </section>
  <div class="brand-small">SAWA</div>
  <p class="dietary-note">* Available as gluten free &amp; vegetarian upon request.</p>

  <div class="dish-photo" role="img" aria-label="Photo of a steaming bowl of Thai curry soup"></div>
  <p class="slogan">Passion to serve you better</p>
  <div class="brand-box">
    <div class="brand-name">SAWA</div>
    <div class="brand-tagline">Traditional Thai Cuisine</div>
  </div>
  <p class="services">Dine-in, Take away &amp; Delivery</p>
  <div class="delivery-offer">
    <p>Free delivery within 5 kms.</p>
    <p>for a minimum order $40</p>
  </div>
  <h2 class="hours-title">Trading Hours</h2>
  <div class="hours">
    <p><b>Lunch:</b> Wed-Sun 11.00-2.30pm</p>
    <p><b>Dinner:</b> 7 days 5.00-9.30pm</p>
  </div>
  <div class="phone"><small>Ph.:</small><span>07 3000 4815</span></div>
  <address class="address">
    52, Lantern Road, Riverbend.<br>(Corner of Ash St. &amp; Lantern Rd.)
  </address>
</main>
</body>
</html>
```